VORK.
BRIDGING HORIZONS
VORK. -
Creative Brief
Use specific fonts
any thing which suits with the LOGO provided
Professional
RAJESH MOTLA
MR.
B.P. No.6213, COMMUNE-3, NEAR TORAVI LAUNDRY, KALEBA ZONE, BAMAKO-MALI
rajesh@vork.co.in
vork.co.in
pls mention MANAGING DIRECTOR, the designation, below the name of the person.
LOGO at centre. Below mentioned address at bottom: India Office D-47, Palm Enclave-II, Gurgaon, Haryana 122015 ph:+91-124-4708352, fax:+91-124-4519267 cell:+91-9871436029

```html
<!DOCTYPE html>
<html lang="en">
<head>
<meta charset="utf-8">
<title>VORK. Business Card Options</title>
<link href="https://fonts.googleapis.com/css2?family=Open+Sans:ital,wght@0,400;0,600;0,800;1,400;1,600&family=Michroma&display=swap" rel="stylesheet">
<style>
  :root {
    --board: #3a3a3a;
    --card: #ffffff;
    --navy: #0b2f7a;
    --blue: #1a5fb4;
    --sky: #4d9be0;
    --green: #7cc242;
    --ink: #333a45;
    --muted: #6a7280;
    --rule: #c9ced6;
    --caption: #e6e6e6;
  }
  * { box-sizing: border-box; margin: 0; padding: 0; }
  html, body { width: 1200px; height: 809px; overflow: hidden; }
  body {
    background: var(--board);
    font-family: "Open Sans", Arial, sans-serif;
    position: relative;
  }
  .card {
    position: absolute;
    width: 432px;
    height: 281px;
    background: var(--card);
    border-radius: 14px;
    overflow: hidden;
    box-shadow: 0 4px 10px rgba(0,0,0,.55);
  }
  .front-a { left: 115px; top: 48px; }
  .front-b { left: 643px; top: 48px; }
  .back-a  { left: 115px; top: 432px; }
  .back-b  { left: 643px; top: 432px; }

  .caption {
    position: absolute;
    width: 432px;
    text-align: center;
    font-family: "Michroma", Arial, sans-serif;
    font-size: 14px;
    letter-spacing: 2px;
    color: var(--caption);
  }

  .top-band { position: absolute; left: 0; top: 0; width: 432px; height: 60px; }

  .brand { position: absolute; display: flex; align-items: center; gap: 10px; }
  .brand-dot { border-radius: 50%; background: var(--blue); flex: none; }
  .brand-name {
    font-weight: 800; color: var(--blue); line-height: 1; letter-spacing: 1px;
  }
  .brand-tag {
    position: absolute; font-weight: 600; color: var(--blue);
    font-size: 10px; letter-spacing: 2.5px;
  }

  .person { position: absolute; color: var(--ink); }
  .person-name { color: var(--blue); font-size: 13px; font-weight: 600; }
  .person-role { font-size: 9px; font-style: italic; color: var(--muted); margin-bottom: 5px; }
  .person-address { font-size: 9px; font-style: italic; line-height: 1.45; color: var(--ink); }

  .divider { position: absolute; width: 1px; background: var(--rule); }

  .contacts { position: absolute; list-style: none; font-size: 9.5px; color: var(--ink); }
  .contacts li { display: flex; align-items: center; gap: 7px; height: 19px; }
  .icon { width: 11px; height: 11px; flex: none; }

  .office { position: absolute; left: 0; width: 432px; text-align: center; color: var(--ink); }
  .office-title { font-size: 14px; font-style: italic; color: var(--blue); margin-bottom: 6px; }
  .office-address { font-size: 11px; display: flex; justify-content: center; align-items: center; gap: 5px; margin-bottom: 8px; }
  .office-phones { font-size: 10.5px; display: flex; justify-content: center; align-items: center; gap: 4px; }
  .office-phones span { display: inline-flex; align-items: center; gap: 3px; }
</style>
</head>
<body>

<svg width="0" height="0" style="position:absolute">
  <defs>
    <linearGradient id="band-fill" x1="0" y1="0" x2="1" y2="0">
      <stop offset="0" stop-color="#0b2f7a"/>
      <stop offset="0.55" stop-color="#1a5fb4"/>
      <stop offset="1" stop-color="#6fb3ec"/>
    </linearGradient>
    <symbol id="band" viewBox="0 0 432 60">
      <path d="M0 0H432V40C300 28 140 30 0 46Z" fill="url(#band-fill)"/>
      <path d="M0 46C140 30 300 28 432 40V44C300 33 140 36 0 52Z" fill="#7cc242"/>
    </symbol>
    <symbol id="i-phone" viewBox="0 0 12 12"><path d="M3 1l2 2.5-1.2 1.2a6 6 0 0 0 3.5 3.5L8.5 7 11 9l-1.2 2C5 11 1 7 1 2.2Z" fill="#1a5fb4"/></symbol>
    <symbol id="i-mobile" viewBox="0 0 12 12"><rect x="3" y="0.5" width="6" height="11" rx="1.2" fill="#1a5fb4"/><rect x="4" y="2" width="4" height="6.5" fill="#fff"/></symbol>
    <symbol id="i-mail" viewBox="0 0 12 12"><circle cx="6" cy="6" r="5.5" fill="#1a5fb4"/><path d="M3 4.2h6v4H3Z" fill="#fff"/><path d="M3 4.2l3 2.2 3-2.2" stroke="#1a5fb4" stroke-width=".8" fill="none"/></symbol>
    <symbol id="i-web" viewBox="0 0 12 12"><circle cx="6" cy="6" r="5.5" fill="#1a5fb4"/><path d="M1 6h10M6 1c-2.5 3-2.5 7 0 10M6 1c2.5 3 2.5 7 0 10" stroke="#fff" stroke-width=".8" fill="none"/></symbol>
    <symbol id="i-home" viewBox="0 0 12 12"><path d="M6 1L1 6h1.6v5h2.8V8h1.2v3h2.8V6H11Z" fill="#1a5fb4"/></symbol>
  </defs>
</svg>

<!-- Front A -->
<section class="card front-a">
  <svg class="top-band"><use href="#band"/></svg>
  <div class="brand" style="left:62px; top:84px;">
    <span class="brand-dot" style="width:42px;height:42px;"></span>
    <span class="brand-name" style="font-size:40px;">VORK</span>
  </div>
  <div class="brand-tag" style="left:116px; top:128px; font-size:8px; letter-spacing:1.6px;">BRIDGING HORIZONS</div>
  <div class="person" style="left:62px; top:160px;">
    <div class="person-name">Rajesh Motla</div>
    <div class="person-role">Managing Director</div>
    <div class="person-address">B.P. No.6213, Commune-3,<br>Near Toravi Laundry,<br>Kaleba Zone,<br>Bamako-Mali</div>
  </div>
  <div class="divider" style="left:226px; top:160px; height:92px;"></div>
  <ul class="contacts" style="left:238px; top:164px;">
    <li><svg class="icon"><use href="#i-phone"/></svg>+223-20486159</li>
    <li><svg class="icon"><use href="#i-mobile"/></svg>+223-76392841</li>
    <li><svg class="icon"><use href="#i-mail"/></svg>rajesh@vork.co.in</li>
    <li><svg class="icon"><use href="#i-web"/></svg>www.vork.co.in</li>
  </ul>
</section>
<div class="caption" style="left:115px; top:360px;">Business Card Front Option A</div>

<!-- Front B -->
<section class="card front-b">
  <svg class="top-band"><use href="#band"/></svg>
  <span class="brand-dot" style="position:absolute; left:92px; top:92px; width:50px; height:50px;"></span>
  <div class="brand" style="left:52px; top:150px;">
    <span class="brand-name" style="font-size:44px;">VORK</span>
  </div>
  <div class="brand-tag" style="left:58px; top:196px;">BRIDGING HORIZONS</div>
  <div class="divider" style="left:254px; top:56px; height:200px;"></div>
  <div class="person" style="left:266px; top:50px;">
    <div class="person-name">Rajesh Motla</div>
    <div class="person-role">Managing Director</div>
    <div class="person-address">B.P. No.6213, Commune-3,<br>Near Toravi Laundry,<br>Kaleba Zone,<br>Bamako-Mali</div>
  </div>
  <ul class="contacts" style="left:266px; top:160px;">
    <li><svg class="icon"><use href="#i-phone"/></svg>+223-20486159</li>
    <li><svg class="icon"><use href="#i-mobile"/></svg>+223-76392841</li>
    <li><svg class="icon"><use href="#i-mail"/></svg>rajesh@vork.co.in</li>
    <li><svg class="icon"><use href="#i-web"/></svg>www.vork.co.in</li>
  </ul>
</section>
<div class="caption" style="left:643px; top:360px;">Business Card Front Option B</div>

<!-- Back A -->
<section class="card back-a">
  <div class="brand" style="left:108px; top:62px;">
    <span class="brand-dot" style="width:58px;height:58px;"></span>
    <span class="brand-name" style="font-size:56px;">VORK</span>
  </div>
  <div class="brand-tag" style="left:186px; top:124px; font-size:11px;">BRIDGING HORIZONS</div>
  <div class="office" style="top:176px;">
    <div class="office-title">India Office</div>
    <div class="office-address"><svg class="icon"><use href="#i-home"/></svg>D-47, Palm Enclave-II, Gurgaon, Haryana 122015</div>
    <div class="office-phones">
      <span><svg class="icon"><use href="#i-phone"/></svg>+91-124-4708352</span>
      <span><svg class="icon"><use href="#i-mobile"/></svg>+91-124-4519267</span>
      <span><svg class="icon"><use href="#i-mobile"/></svg>+91-9871436029</span>
    </div>
  </div>
</section>
<div class="caption" style="left:115px; top:740px;">Business Card Back Option A</div>

<!-- Back B -->
<section class="card back-b">
  <div class="brand" style="left:128px; top:76px;">
    <span class="brand-dot" style="width:58px;height:58px;"></span>
    <span class="brand-name" style="font-size:44px;">VORK</span>
  </div>
  <div class="office" style="top:176px;">
    <div class="office-title">India Office</div>
    <div class="office-address"><svg class="icon"><use href="#i-home"/></svg>D-47, Palm Enclave-II, Gurgaon, Haryana 122015</div>
    <div class="office-phones">
      <span><svg class="icon"><use href="#i-phone"/></svg>+91-124-4708352</span>
      <span><svg class="icon"><use href="#i-mobile"/></svg>+91-124-4519267</span>
      <span><svg class="icon"><use href="#i-mobile"/></svg>+91-9871436029</span>
    </div>
  </div>
</section>
<div class="caption" style="left:643px; top:740px;">Business Card Back Option B</div>

</body>
</html>
```